I am looking for book cover design title of the book is ELDERS AND LANTERNISTS KEEP HOLLOW WEDNESDAY
Vertical half of the book is to be Jewish flag with star of David and the other half is to be Lanternists logo , background in light will be a moon

```html
<!DOCTYPE html>
<html lang="en">
<head>
<meta charset="utf-8">
<title>Elders and Lanternists Keep Hollow Wednesday — Book Cover</title>
<link rel="stylesheet" href="https://fonts.googleapis.com/css2?family=Archivo+Narrow:wght@700&display=swap">
<style>
  :root {
    --night: #000000;
    --ink-white: #ffffff;
    --flag-blue: #0038b8;
    --flag-blue-light: #5a8cff;
    --mark-blue: #1a5ae0;
    --mist: #dcdcdc;
    --mist-dark: #a9a9a9;
  }
  html, body {
    margin: 0;
    padding: 0;
    width: 1012px;
    height: 1200px;
    overflow: hidden;
    background: var(--night);
  }
  .cover {
    position: relative;
    width: 1012px;
    height: 1200px;
    overflow: hidden;
    background:
      linear-gradient(180deg, var(--night) 0%, var(--night) 66%, #4a4a4a 75%, var(--mist-dark) 80%, var(--mist) 90%, #f4f4f4 100%);
    font-family: "Archivo Narrow", "Arial Narrow", sans-serif;
  }
  .moon-glow {
    position: absolute;
    left: 0;
    top: 760px;
    width: 1012px;
    height: 320px;
    background: radial-gradient(ellipse 45% 40% at 50% 45%, rgba(255,255,255,0.95) 0%, rgba(255,255,255,0.35) 55%, rgba(255,255,255,0) 100%);
  }
  .moon {
    position: absolute;
    left: 266px;
    top: 372px;
    width: 470px;
    height: 470px;
    border-radius: 50%;
    background: radial-gradient(circle at 55% 45%, #f2f6f8 0%, #c9d3da 40%, #8c9aa5 75%, #4d5a64 100%);
    box-shadow: 0 0 80px 20px rgba(255,255,255,0.25);
  }
  .title {
    position: absolute;
    left: 0;
    top: 64px;
    width: 1012px;
    margin: 0;
    color: var(--ink-white);
    text-align: center;
    font-weight: 700;
    font-size: 72px;
    line-height: 108px;
    letter-spacing: 0.5px;
  }
  .title-line { display: block; }
  .title-middle {
    display: flex;
    align-items: center;
    justify-content: center;
    gap: 26px;
  }
  .title-rule {
    width: 132px;
    height: 3px;
    background: var(--ink-white);
  }
  .flag {
    position: absolute;
    left: 0;
    top: 899px;
    width: 515px;
    height: 270px;
  }
  .mark {
    position: absolute;
    left: 630px;
    top: 1015px;
    display: flex;
    align-items: center;
    gap: 14px;
    color: var(--mark-blue);
    font-weight: 700;
    font-size: 52px;
  }
  .mark-dot {
    width: 30px;
    height: 30px;
    border-radius: 50%;
    background: var(--mark-blue);
  }
</style>
</head>
<body>
  <main class="cover">
    <div class="moon-glow"></div>
    <div class="moon" role="img" aria-label="Photograph of a full moon glowing in a starry night sky"></div>

    <h1 class="title">
      <span class="title-line">ELDERS AND LANTERNISTS</span>
      <span class="title-line title-middle"><span class="title-rule"></span>KEEP<span class="title-rule"></span></span>
      <span class="title-line">HOLLOW WEDNESDAY</span>
    </h1>

    <svg class="flag" viewBox="0 0 515 270" aria-label="Flag with Star of David">
      <defs>
        <linearGradient id="bandTop" x1="0" x2="1" y1="0" y2="0">
          <stop offset="0" stop-color="var(--flag-blue)"/>
          <stop offset="0.45" stop-color="var(--flag-blue)"/>
          <stop offset="1" stop-color="var(--flag-blue-light)"/>
        </linearGradient>
        <linearGradient id="field" x1="0" x2="1" y1="0" y2="0">
          <stop offset="0" stop-color="#d4d4d4"/>
          <stop offset="1" stop-color="#ffffff"/>
        </linearGradient>
      </defs>
      <rect x="0" y="0" width="515" height="270" fill="url(#field)"/>
      <rect x="0" y="0" width="515" height="51" fill="url(#bandTop)"/>
      <rect x="0" y="219" width="515" height="51" fill="var(--flag-blue)"/>
      <g fill="none" stroke="var(--flag-blue)" stroke-width="10" stroke-linejoin="miter">
        <polygon points="257,71 318,170 196,170"/>
        <polygon points="257,205 318,106 196,106"/>
      </g>
    </svg>

    <div class="mark"><span class="mark-dot"></span>Lanternists</div>
  </main>
</body>
</html>
```